Mine Engineering Consultancy specializing in
* Pit optimization
* Mine Design
* Scheduling
* Mine Rehabilitation

Industry/Entity Type

Mining

Contact Information for Business Card

RVT Mining Pty Ltd
Derek Holloway
Director/Principle Mining Engineer
Mobile 0413582961
Email derek.holloway@rvtmining-example.com

```html
<!DOCTYPE html>
<html lang="en">
<head>
<meta charset="utf-8">
<title>RVT Mining Pty Ltd – Business Card</title>
<link rel="stylesheet" href="https://fonts.googleapis.com/css2?family=Arimo:wght@400;700&family=Tinos&display=swap">
<style>
  :root {
    --backdrop: #dadada;
    --card-white: #f7f7f6;
    --card-dark: #1d1d1e;
    --card-dark-soft: #2a2a2b;
    --brand-blue: #1d6fc1;
    --text-light: #f2f2f2;
    --text-muted: #b9b9b9;
  }
  * { box-sizing: border-box; margin: 0; padding: 0; }
  html, body {
    width: 1200px;
    height: 900px;
    overflow: hidden;
    background: var(--backdrop);
  }
  .stage {
    position: relative;
    width: 1200px;
    height: 900px;
  }
  .card {
    position: absolute;
    width: 490px;
    height: 280px;
    border-radius: 3px;
    box-shadow: 0 6px 18px rgba(0,0,0,0.12);
    overflow: hidden;
  }

  /* Front: company name */
  .card--front {
    left: 75px;
    top: 310px;
    background: var(--card-white);
  }
  .brand-name {
    position: absolute;
    left: 62px;
    top: 112px;
    display: flex;
    align-items: center;
    gap: 14px;
    font-family: "Tinos", "Times New Roman", serif;
    font-size: 38px;
    color: var(--brand-blue);
    white-space: nowrap;
  }
  .brand-mark {
    width: 14px;
    height: 14px;
    background: var(--brand-blue);
  }

  /* Back: contact details */
  .card--back {
    left: 635px;
    top: 310px;
  }
  .card-texture {
    position: absolute;
    inset: 0;
    background: linear-gradient(135deg, var(--card-dark-soft) 0%, var(--card-dark) 60%, #161617 100%);
  }
  .contact {
    position: absolute;
    inset: 0;
    font-family: "Arimo", Arial, sans-serif;
  }
  .person-name {
    position: absolute;
    left: 44px;
    top: 86px;
    font-size: 28px;
    font-weight: 700;
    letter-spacing: 0.5px;
    color: var(--text-light);
    text-transform: uppercase;
  }
  .person-name .surname { color: var(--brand-blue); }
  .person-role {
    position: absolute;
    left: 45px;
    top: 122px;
    font-size: 10px;
    color: var(--text-muted);
  }
  .contact-line {
    position: absolute;
    display: flex;
    align-items: center;
    gap: 10px;
    font-size: 12px;
    color: var(--text-light);
  }
  .contact-line--email { left: 44px; top: 168px; }
  .contact-line--phone { left: 44px; top: 206px; }
  .contact-icon {
    width: 22px;
    height: 22px;
    background: var(--brand-blue);
    border-radius: 2px;
    display: flex;
    align-items: center;
    justify-content: center;
  }
</style>
</head>
<body>
<main class="stage">

  <section class="card card--front" aria-label="Business card front">
    <div class="brand-name">
      <span class="brand-mark"></span>
      <span>RVT Mining Pty Ltd</span>
    </div>
  </section>

  <section class="card card--back" aria-label="Business card back">
    <div class="card-texture" role="img" aria-label="Subtle dark geometric triangle pattern"></div>
    <div class="contact">
      <h1 class="person-name">Derek <span class="surname">Holloway</span></h1>
      <p class="person-role">Director/Principle Mining Engineer</p>

      <p class="contact-line contact-line--email">
        <span class="contact-icon">
          <svg width="14" height="10" viewBox="0 0 14 10" aria-hidden="true">
            <rect x="0.5" y="0.5" width="13" height="9" fill="none" stroke="#fff" stroke-width="1"/>
            <polyline points="0.5,0.5 7,5.5 13.5,0.5" fill="none" stroke="#fff" stroke-width="1"/>
          </svg>
        </span>
        derek.holloway@rvtmining-example.com
      </p>

      <p class="contact-line contact-line--phone">
        <span class="contact-icon">
          <svg width="12" height="14" viewBox="0 0 12 14" aria-hidden="true">
            <path d="M3 1 L5 4 L3.8 5.4 Q5 8.6 7.6 10.2 L9 9 L11.5 11 L10 13 Q3.5 12 1.2 3.2 Z" fill="#fff"/>
          </svg>
        </span>
        Mobile 0413582961
      </p>
    </div>
  </section>

</main>
</body>
</html>
```